Bright Harbor Motors Business Card

Would like a cutting edge / high end Automotive Business card design. Please see current card which is old and dated. Would like to maintain the Bright Harbor Motors logo and same information (address, website, etc).

See our website for the look and feel of what we offer - www.brightharbormotors.example

Target Market(s)

Upper class car buyers

Contact Information for Business Card

Modern high end business card design

Requirements
Nice to have
• Carbon Fiber look background

```html
<!DOCTYPE html>
<html lang="en">
<head>
<meta charset="utf-8">
<title>Bright Harbor Motors – Business Card</title>
<link rel="stylesheet" href="https://fonts.googleapis.com/css2?family=Poppins:wght@300;400;600;700&display=swap">
<style>
  :root {
    --stage: #1c1c1d;
    --card-top: #343435;
    --card-bottom: #1a1a1b;
    --band-dark: #141414;
    --band-mid: #2b2b2c;
    --ink: #f2f2f2;
    --ink-soft: #c9c9c9;
    --ink-muted: #8d8d8d;
    --rule: #9a9a9a;
  }
  * { margin: 0; padding: 0; box-sizing: border-box; }
  html, body { width: 1200px; height: 900px; overflow: hidden; background: var(--stage); }
  body { font-family: "Poppins", sans-serif; color: var(--ink); }

  .stage {
    position: relative; width: 1200px; height: 900px;
    display: flex; justify-content: center; align-items: center; gap: 70px;
  }
  .card {
    position: relative; width: 340px; height: 595px;
    background: linear-gradient(160deg, var(--card-top), var(--card-bottom) 75%);
    box-shadow: 0 18px 40px rgba(0,0,0,.55);
    overflow: hidden;
    display: flex; flex-direction: column; align-items: center;
  }
  .card__band {
    position: absolute; top: 0; bottom: 0; width: 46px;
    background: linear-gradient(90deg, var(--band-dark), var(--band-mid) 50%, var(--band-dark));
  }
  .card__band--left { left: 0; }
  .card__band--right { right: 0; }

  .brand { text-align: center; margin-top: 78px; }
  .brand__name {
    font-weight: 600; font-size: 27px; line-height: 1.12; color: var(--ink);
    letter-spacing: .5px;
  }
  .brand__rule { width: 210px; height: 1px; background: var(--rule); margin: 10px auto 0; }

  .values {
    margin-top: 12px; font-size: 11.5px; font-weight: 300; letter-spacing: 1.2px;
    color: var(--ink-soft); display: flex; gap: 12px; align-items: center;
  }
  .values__sep { width: 2px; height: 13px; background: var(--ink); }

  .person { text-align: center; margin-top: 50px; }
  .person__name { font-weight: 700; font-size: 24px; letter-spacing: .5px; }
  .person__role { font-weight: 400; font-size: 14px; letter-spacing: 1px; color: var(--ink-soft); margin-top: 2px; }

  .icons { display: flex; gap: 14px; margin-top: 38px; }
  .icon {
    width: 28px; height: 28px; border-radius: 50%; background: var(--ink);
    display: flex; align-items: center; justify-content: center;
  }
  .icon svg { width: 15px; height: 15px; fill: #1c1c1d; }

  .contact { text-align: center; margin-top: 34px; font-size: 14.5px; line-height: 1.9; color: var(--ink); }
  .contact__email { font-size: 12px; font-weight: 300; color: var(--ink-soft); }
  .contact__web { font-size: 12px; font-weight: 300; color: var(--ink-soft); }
  .contact__web strong { font-weight: 600; color: var(--ink); }

  .dash { width: 20px; height: 3px; background: var(--ink); margin-top: 16px; }

  .address { text-align: center; margin-top: 16px; font-size: 13px; line-height: 1.45; color: var(--ink-muted); }

  .card--back .brand { margin-top: 110px; }
  .tagline {
    margin-top: 18px; text-align: center; font-size: 14px; line-height: 1.4;
    color: var(--ink-soft);
  }
</style>
</head>
<body>
<main class="stage">

  <section class="card card--front" aria-label="Business card front">
    <div class="card__band card__band--left" role="img" aria-label="Carbon fibre texture band"></div>
    <div class="card__band card__band--right" role="img" aria-label="Carbon fibre texture band"></div>

    <div class="brand">
      <p class="brand__name">Bright Harbor<br>Motors</p>
      <div class="brand__rule"></div>
    </div>
    <p class="values">
      <span>QUALITY</span><span class="values__sep"></span>
      <span>INTEGRITY</span><span class="values__sep"></span>
      <span>SERVICE</span>
    </p>

    <div class="person">
      <p class="person__name">DANIEL VARO</p>
      <p class="person__role">OWNER</p>
    </div>

    <div class="icons">
      <span class="icon" aria-label="Phone"><svg viewBox="0 0 24 24"><path d="M6.6 10.8a15.1 15.1 0 0 0 6.6 6.6l2.2-2.2c.3-.3.7-.4 1-.2 1.1.4 2.3.6 3.6.6.6 0 1 .4 1 1V20c0 .6-.4 1-1 1A17 17 0 0 1 3 4c0-.6.4-1 1-1h3.5c.6 0 1 .4 1 1 0 1.3.2 2.5.6 3.6.1.3 0 .7-.2 1z"/></svg></span>
      <span class="icon" aria-label="Fax"><svg viewBox="0 0 24 24"><path d="M6 3h12v5H6zM4 9h16a2 2 0 0 1 2 2v6h-4v4H6v-4H2v-6a2 2 0 0 1 2-2zm4 7v3h8v-3z"/></svg></span>
      <span class="icon" aria-label="Email"><svg viewBox="0 0 24 24"><path d="M2 5h20v14H2zm2 2v.5l8 5 8-5V7zm0 3v7h16v-7l-8 5z"/></svg></span>
      <span class="icon" aria-label="Website"><svg viewBox="0 0 24 24"><path d="M10.6 13.4a1 1 0 0 1 0-1.4l3.5-3.5a1 1 0 1 1 1.4 1.4L12 13.4a1 1 0 0 1-1.4 0zM7 18.5a3.5 3.5 0 0 1 0-5l2-2 1.4 1.4-2 2a1.5 1.5 0 0 0 2.1 2.1l2-2 1.4 1.4-2 2a3.5 3.5 0 0 1-4.9.1zm6.6-7.4 2-2a1.5 1.5 0 0 0-2.1-2.1l-2 2L10.1 7.6l2-2a3.5 3.5 0 0 1 5 5l-2 2z"/></svg></span>
    </div>

    <div class="contact">
      <p>(415) 555-0148</p>
      <p>(415) 555-0172</p>
      <p class="contact__email">daniel@brightharbormotors.example</p>
      <p class="contact__web">www.<strong>brightharbormotors</strong>.example</p>
    </div>

    <div class="dash"></div>

    <p class="address">1180 Lantern Bay Road A<br>Marlow CA 94999</p>
  </section>

  <section class="card card--back" aria-label="Business card back">
    <div class="card__band card__band--left" role="img" aria-label="Carbon fibre texture band"></div>
    <div class="card__band card__band--right" role="img" aria-label="Carbon fibre texture band"></div>

    <div class="brand">
      <p class="brand__name">Bright Harbor<br>Motors</p>
      <div class="brand__rule"></div>
    </div>
    <p class="tagline">Offering the Finest in<br>Luxury and Exotic<br>Sports Cars</p>
  </section>

</main>
</body>
</html>
```